Lifecoach needs website design based on a standard Wordpress theme

I need a website for my new lifecoaching business that can be easily implemented in Wordpress, it needs to be compatible with a standard Wordpress theme. So I can place the pictures, texts etc. in a standard theme of Wordpress.

I want the design to be a very good feeling and playfull one, based on my logo.

Target Market(s)

I will coach people to reach their goals and dreams in life.

Industry/Entity Type

Business

Requirements
Must have
• Can be easy implemented in Wordpress.
Nice to have
• Photo's of nature are nice.

```html
<!DOCTYPE html>
<html lang="en">
<head>
<meta charset="utf-8">
<title>Lena van Dijk Lifecoach</title>
<link href="https://fonts.googleapis.com/css2?family=Source+Sans+3:wght@400;600&display=swap" rel="stylesheet">
<style>
:root{
  --brand:#1a6fb0;
  --brand-light:#2a9fd8;
  --text:#555;
  --muted:#8a8a8a;
  --card-bg:#e6e6e6;
  --rule:#d4d4d4;
  --footer:#000;
  --white:#fff;
}
*{margin:0;padding:0;box-sizing:border-box}
html,body{width:1016px;height:1200px;overflow:hidden;background:var(--white)}
body{font-family:"Source Sans 3",Arial,sans-serif;color:var(--text);position:relative}
.abs{position:absolute}

/* header */
.site-header{left:0;top:0;width:1016px;height:110px;border-bottom:2px solid #e4eaf0;box-shadow:0 2px 3px rgba(0,0,0,.06)}
.brand-mark{left:104px;top:22px;width:72px;height:72px;border-radius:50%;border:4px solid var(--brand-light)}
.brand-name{left:185px;top:36px;font-size:25px;color:var(--brand);letter-spacing:1px;text-transform:uppercase;line-height:1}
.brand-tag{left:235px;top:64px;font-size:15px;color:var(--brand);letter-spacing:1.5px;text-transform:uppercase;line-height:1}
.social{top:8px;width:28px;height:28px;border-radius:50%}
.social.s1{left:779px;background:#2d5c9e}
.social.s2{left:812px;background:#2aa6e0}
.social.s3{left:846px;background:#d33a2c}
.social.s4{left:880px;background:#2c8fc7}
.main-nav{top:62px;font-size:15px;color:var(--brand)}
.main-nav a{position:absolute;color:inherit;text-decoration:none;white-space:nowrap}

/* hero */
.hero{left:0;top:112px;width:1016px;height:383px;background:
  radial-gradient(ellipse at 15% 30%,rgba(255,240,200,.75),transparent 45%),
  radial-gradient(ellipse at 70% 90%,rgba(120,50,10,.55),transparent 55%),
  linear-gradient(100deg,#d39a52 0%,#c9782c 40%,#b86424 70%,#a9521d 100%)}
.hero-text{left:427px;top:151px;font-size:24px;line-height:31px;color:var(--white);white-space:nowrap}
.slider-dot{left:905px;width:10px;height:9px;background:var(--white)}
.slider-dot.active{background:#1c5a8a}

/* feature cards */
.card{top:504px;width:202px;height:218px;background:var(--card-bg)}
.card-media{left:0;top:0;width:202px;height:151px}
.card-text{left:9px;top:159px;width:188px;font-size:10.5px;line-height:13px;color:#333}
.preview{left:78px;top:61px;width:46px;height:46px;border-radius:50%;background:rgba(255,255,255,.55)}
.preview-label{left:0;top:115px;width:202px;text-align:center;font-size:10.5px;color:var(--white)}

/* intro */
.rule{left:146px;width:822px;border-top:1px dashed var(--rule)}
.intro{left:0;top:760px;width:1016px;text-align:center;font-size:16.5px;line-height:21px;color:#7d7d7d}

/* columns */
.col-heading{font-size:20px;color:#555;white-space:nowrap}
.col-sub{font-size:8.5px;color:#666}
.col-body{width:224px;font-size:10.6px;line-height:20.3px;color:var(--muted);text-align:justify}
.col-body p+p{margin-top:20.3px}
.vrule{top:857px;height:274px;border-left:1px dashed var(--rule)}
.blog-heading{color:#999}
.blog-thumb{left:678px;width:46px;height:43px;border-radius:7px}
.blog-title{left:735px;font-size:10.5px;color:#333}
.blog-date{left:735px;font-size:10.5px;color:var(--muted)}

/* footer */
.site-footer{left:0;top:1145px;width:1016px;height:55px;background:var(--footer)}
.footer-nav a{position:absolute;top:22px;font-size:10.5px;color:var(--white);text-decoration:none;white-space:nowrap}
.copyright{left:760px;top:22px;font-size:10.5px;color:var(--white)}
</style>
</head>
<body>

<header class="site-header abs">
  <div class="brand-mark abs"></div>
  <div class="brand-name abs">Lena van Dijk</div>
  <div class="brand-tag abs">Lifecoach</div>

  <div class="social s1 abs" aria-label="Social profile"></div>
  <div class="social s2 abs" aria-label="Social profile"></div>
  <div class="social s3 abs" aria-label="Social profile"></div>
  <div class="social s4 abs" aria-label="Social profile"></div>

  <nav class="main-nav abs" style="left:0;width:1016px">
    <a href="#" style="left:539px">Home</a>
    <a href="#" style="left:607px">About Us</a>
    <a href="#" style="left:695px">Services</a>
    <a href="#" style="left:776px">Blog</a>
    <a href="#" style="left:833px">Contact Us</a>
  </nav>
</header>

<section class="hero abs" role="img" aria-label="Sunlit meadow of wild flowers in warm golden light">
  <p class="hero-text abs">We specialize in transition life coaching<br>for personal and professional empowerment.</p>
  <span class="slider-dot active abs" style="top:300px"></span>
  <span class="slider-dot abs" style="top:318px"></span>
  <span class="slider-dot abs" style="top:336px"></span>
  <span class="slider-dot abs" style="top:354px"></span>
</section>

<article class="card abs" style="left:92px">
  <div class="card-media abs" role="img" aria-label="Woman relaxing with a book in a bright room" style="background:linear-gradient(120deg,#b9c4ae,#dcdcd4 55%,#cfc6bb)"></div>
  <div class="preview abs">
    <svg width="46" height="46" viewBox="0 0 46 46"><circle cx="25" cy="20" r="7" fill="none" stroke="#666" stroke-width="3"/><line x1="20" y1="25" x2="13" y2="32" stroke="#666" stroke-width="4" stroke-linecap="round"/></svg>
  </div>
  <div class="preview-label abs">Preview</div>
  <p class="card-text abs">Neque porro quisquam est, qui dolorem ipsum quia dolor sit amet, consectetur, adipisci velit.</p>
</article>

<article class="card abs" style="left:302px">
  <div class="card-media abs" role="img" aria-label="Two people walking on a forest path" style="background:linear-gradient(90deg,#2f3f2a,#56684a 50%,#7a7c70)"></div>
  <p class="card-text abs">Neque porro quisquam est, qui dolorem ipsum quia dolor sit amet, consectetur, adipisci velit.</p>
</article>

<article class="card abs" style="left:512px">
  <div class="card-media abs" role="img" aria-label="Person raising arms at a lake at dusk" style="background:linear-gradient(180deg,#6b706a,#4a4f47 55%,#2f332e)"></div>
  <p class="card-text abs">Neque porro quisquam est, qui dolorem ipsum quia dolor sit amet, consectetur, adipisci velit.</p>
</article>

<article class="card abs" style="left:722px">
  <div class="card-media abs" role="img" aria-label="Climbers on a rock against a blue sky" style="background:linear-gradient(180deg,#2a4a78,#1f3862 60%,#162a4a)"></div>
  <p class="card-text abs">Neque porro quisquam est, qui dolorem ipsum quia dolor sit amet, consectetur, adipisci velit.</p>
</article>

<div class="rule abs" style="top:737px"></div>
<p class="intro abs">Hello, my name is “Your Name” and I specialize in Front-End Web Development.<br>I aim to create vibrant, detailed designs while keeping web standards and usability aspects in mind.</p>
<div class="rule abs" style="top:830px"></div>

<!-- column one -->
<svg class="abs" style="left:144px;top:855px" width="28" height="26" viewBox="0 0 28 26"><path d="M14 24 C4 16 1 12 1 8 C1 4 4 1 8 1 C11 1 13 3 14 5 C15 3 17 1 20 1 C24 1 27 4 27 8 C27 12 24 16 14 24Z" fill="#e0452e"/></svg>
<h2 class="col-heading abs" style="left:181px;top:851px;font-weight:400">Lorem Ipsum Dolor</h2>
<div class="col-sub abs" style="left:180px;top:879px">Sub Heading Goes Here</div>
<div class="col-body abs" style="left:146px;top:908px">
  <p>Lorem ipsum dolor sit amet, consectetur adipiscing elit. Pellentesque id leo id lectus aliquam convallis. Nam sodales consectetur est, placerat auctor arcu volutpat a.</p>
  <p>Nunc ipsum libero, malesuada id dapibus a, pulvinar nec mi. Fusce interdum fermentum elit quis laoreet. Donec dignissim lectus id nibh commodo congue.</p>
</div>
<div class="vrule abs" style="left:394px"></div>

<!-- column two -->
<svg class="abs" style="left:412px;top:855px" width="28" height="26" viewBox="0 0 28 26"><rect x="2" y="1" width="24" height="17" rx="1" fill="#bbb"/><rect x="4" y="3" width="20" height="13" fill="#4a4a4a"/><rect x="11" y="18" width="6" height="4" fill="#aaa"/><rect x="7" y="22" width="14" height="2" fill="#ccc"/></svg>
<h2 class="col-heading abs" style="left:450px;top:851px;font-weight:400">Lorem Ipsum Dolor</h2>
<div class="col-sub abs" style="left:448px;top:879px">Sub Heading Goes Here</div>
<div class="col-body abs" style="left:414px;top:908px">
  <p>Lorem ipsum dolor sit amet, consectetur adipiscing elit. Pellentesque id leo id lectus aliquam convallis. Nam sodales consectetur est, placerat auctor arcu volutpat a.</p>
  <p>Nunc ipsum libero, malesuada id dapibus a, pulvinar nec mi. Fusce interdum fermentum elit quis laoreet. Donec dignissim lectus id nibh commodo congue.</p>
</div>
<div class="vrule abs" style="left:660px"></div>

<!-- blog column -->
<svg class="abs" style="left:679px;top:855px" width="28" height="24" viewBox="0 0 28 24"><rect x="1" y="2" width="26" height="20" rx="2" fill="#f4f4f4" stroke="#bbb"/><line x1="5" y1="8" x2="23" y2="8" stroke="#bbb"/><line x1="5" y1="12" x2="23" y2="12" stroke="#bbb"/><line x1="5" y1="16" x2="18" y2="16" stroke="#bbb"/></svg>
<h2 class="col-heading blog-heading abs" style="left:719px;top:851px;font-weight:400">Fresh From The Blog</h2>

<div class="blog-thumb abs" style="top:908px;background:linear-gradient(135deg,#d9b24a,#b8452e)" role="img" aria-label="Blog post photo of a couple in autumn leaves"></div>
<div class="blog-title abs" style="top:909px">Lorem Ipsum Dolor Amet.</div>
<div class="blog-date abs" style="top:924px">May 25, 2001</div>

<div class="blog-thumb abs" style="top:962px;background:linear-gradient(180deg,#c9ced4,#7c8088)" role="img" aria-label="Blog post photo of a person on a road"></div>
<div class="blog-title abs" style="top:963px">Lorem Ipsum Dolor Amet.</div>
<div class="blog-date abs" style="top:978px">May 25, 2001</div>

<div class="blog-thumb abs" style="top:1016px;background:linear-gradient(180deg,#c8cdd0,#6e5a45)" role="img" aria-label="Blog post photo of a climber on a summit"></div>
<div class="blog-title abs" style="top:1018px">Lorem Ipsum Dolor Amet.</div>
<div class="blog-date abs" style="top:1033px">May 25, 2001</div>

<div class="blog-thumb abs" style="top:1070px;background:linear-gradient(135deg,#8fa3c4,#e4e0dc)" role="img" aria-label="Blog post photo of a business team"></div>
<div class="blog-title abs" style="top:1072px">Lorem Ipsum Dolor Amet.</div>
<div class="blog-date abs" style="top:1087px">May 25, 2001</div>

<footer class="site-footer abs">
  <nav class="footer-nav">
    <a href="#" style="left:144px">Home</a>
    <a href="#" style="left:193px">About Us</a>
    <a href="#" style="left:257px">Services</a>
    <a href="#" style="left:314px">Blog</a>
    <a href="#" style="left:356px">Contact Us</a>
  </nav>
  <div class="copyright abs">© 2014.www.companyname.com</div>
</footer>

</body>
</html>
```